依頼詳細
洗練された新しい雰囲気のデザインでお願いいたします!
※イメージは下記URLを参考にしてください。
http://hoshizorabooks.jp/kanade/back/

■ターゲット
新しい働き方に興味がある方々

■サイズ
A5

■仕様
・A5版(148×210㎜)
・天地210mm(+版面天地各3 mmつけてください)
・左右148mm(+表1 ・4の背でない方に版面3mmつけてください)
・背幅:5mm
・本文は横書き、左綴じになります。
・表紙(表1、表4、背):4C(フルカラー)
・カバー、帯をつける予定はございません。
記載項目
タイトル:『朝と窓辺から広がる自由な仕事道』
サブタイトル:『~千の机が描く日々~』
編著:ミツバリンク株式会社

素材として弊社ロゴを添付いたしますが、使用の有無はお任せいたします。
希望イメージ
シンプル 複雑
単色 カラフル
暗い 明るい
日常 高級
遊び心 厳粛
未来的 伝統的
女性的 男性的
希望する色
納品ファイル
• 高解像度JPG (.jpg)
• イラストレーター形式 (.ai)
補足説明
ミツバリンクのコーポレートカラーである「青色」を基調に制作をお願いします。

ご提案いただいたデザインに対して、修正をお願いすることがあります。
当選後に、文字修正を含めた最終調整を行った上で、入稿データを作成いただくことになります。
出版バーコード、定価等は後ほど当選者に送付いたします。
依頼をご覧いただいた皆様、提案いただいた皆様、誠にありがとうございます。

追加で2点要望をお伝えいたします。

1.依頼文にも記載しましたとおり、今回は洗練させたイメージのデザインにしたいと考えております。弊社キャラクターのミツバリンク君を大きく使ってしまうとポップな印象になるかと思いますので、小さめに使う、もしくは使わないデザインで希望いたします。

2.青色を基調としたデザインでお願いしましたが、せっかくのフルカラーの表紙ですので青がより引き立つよう、
・ポイント的に他の色味を使っていただく
・タイトルの文字色を変える
等、工夫いただけるとよいかと思います。

締め切りまで残りわずかですが、引き続きどうぞ宜しくお願いいたします。
■ 選んだ理由

本のイメージを見事に反映していただいたことと、提案理由に大変納得したことが選んだ理由です。
「仕事術の解説でもなく、超有名クリエイターの紹介でもない。あくまで多様なフリーランスの方々のライフスタイルを伝えることがこの書籍の目的であると思います。」(sorafune様の提案コメントから抜粋。)
上記部分は、想いを見事汲み取っていただき、大変嬉しかったです。
明瞭なビジュアルデザインと、全体的に清潔で明るいイメージにまとめていただき、イラストも可愛らしく作っていただきました。
素敵な作品をありがとうございました!

■ 提案者全員のお礼・コメント

この度のカバーデザインコンテストに参加いただきました皆様、本当にありがとうございました。
非常に多くの作品をご提案いただき、選定に迷うほどでした。
4月以降に書籍が発売予定ですので、お買い求めいただければ幸いです。

```html
<!DOCTYPE html>
<html lang="ja">
<head>
<meta charset="utf-8">
<title>朝と窓辺から広がる自由な仕事道</title>
<link rel="stylesheet" href="https://fonts.googleapis.com/css2?family=Noto+Sans+JP:wght@500;700;900&family=Roboto+Mono:wght@400;700&display=swap">
<style>
  :root {
    --brand-blue: #1a6fc2;
    --ink: #333a40;
    --paper: #ffffff;
    --mascot-tone: #cfe0f2;
  }
  * { margin: 0; padding: 0; box-sizing: border-box; }
  html, body { width: 844px; height: 1200px; overflow: hidden; background: var(--paper); }
  .cover {
    position: relative;
    width: 844px;
    height: 1200px;
    background: var(--paper);
    font-family: "Noto Sans JP", sans-serif;
  }
  .mascot {
    position: absolute;
    left: 22px;
    top: 14px;
    width: 80px;
    height: 72px;
    border-radius: 10px;
    background: linear-gradient(160deg, var(--mascot-tone), #8fb6df);
  }
  .title {
    position: absolute;
    top: 172px;
    right: 178px;
    writing-mode: vertical-rl;
    font-weight: 900;
    font-size: 94px;
    line-height: 1.34;
    letter-spacing: 0;
    color: var(--brand-blue);
  }
  .title span { display: block; }
  .subtitle {
    position: absolute;
    top: 268px;
    left: 236px;
    writing-mode: vertical-rl;
    font-weight: 700;
    font-size: 30px;
    letter-spacing: 0.08em;
    color: var(--ink);
  }
  .tagline {
    position: absolute;
    left: 292px;
    top: 852px;
    width: 370px;
    font-family: "Roboto Mono", monospace;
    color: var(--brand-blue);
    text-align: justify;
  }
  .tagline .lead {
    display: block;
    font-size: 44px;
    font-weight: 400;
    line-height: 1.1;
    letter-spacing: 0.01em;
  }
  .tagline .word {
    display: block;
    font-size: 62px;
    font-weight: 700;
    line-height: 1.05;
    letter-spacing: -0.01em;
  }
  .publisher {
    position: absolute;
    left: 290px;
    top: 1030px;
    color: var(--brand-blue);
  }
  .publisher .name {
    display: block;
    font-size: 40px;
    font-weight: 900;
    line-height: 1.1;
  }
  .publisher .credit {
    display: block;
    margin-top: 14px;
    font-size: 22px;
    font-weight: 500;
    color: var(--ink);
  }
</style>
</head>
<body>
  <main class="cover">
    <div class="mascot" role="img" aria-label="小さなミツバリンク君のキャラクターイラスト"></div>

    <h1 class="title">
      <span>朝と窓辺から</span>
      <span>広がる自由な</span>
      <span>仕事道</span>
    </h1>

    <p class="subtitle">〜千の机が描く日々〜</p>

    <p class="tagline">
      <span class="lead">Life Style of</span>
      <span class="word">FREELANCER</span>
    </p>

    <div class="publisher">
      <span class="name">ミツバリンク</span>
      <span class="credit">編著：ミツバリンク株式会社</span>
    </div>
  </main>
</body>
</html>
```